Maple Ridge business card design

Card needs to include the following text/items:
Company Logo
Tobin Marsh
Phone # - 555-318-7642
service@mapleridgelandscaping.example
Lawn & landscape maintenance services

```html
<!DOCTYPE html>
<html lang="en">
<head>
<meta charset="utf-8">
<title>Maple Ridge Landscaping – Business Card</title>
<link rel="stylesheet" href="https://fonts.googleapis.com/css2?family=Cinzel:wght@700&family=Arimo:wght@400&display=swap">
<style>
  :root {
    --backdrop: #2b2b2b;
    --card-white: #ffffff;
    --forest: #0c4a2a;
    --leaf: #5aa83c;
    --ink: #222222;
    --mark-fill: #2f7a3e;
  }
  * { margin: 0; padding: 0; box-sizing: border-box; }
  html, body {
    width: 1200px; height: 1059px; overflow: hidden;
    background: var(--backdrop);
  }
  .stage { position: relative; width: 1200px; height: 1059px; }
  .card {
    position: absolute;
    border-radius: 20px;
    overflow: hidden;
    box-shadow: 0 10px 24px rgba(0,0,0,.55);
  }
  .card--front { left: 256px; top: 89px; width: 688px; height: 390px; background: var(--card-white); }
  .card--back  { left: 254px; top: 547px; width: 693px; height: 393px; background: var(--forest); }

  .brand { position: absolute; text-align: center; font-family: "Cinzel", serif; font-weight: 700; }
  .brand__mark { display: block; margin: 0 auto; border-radius: 50%; background: var(--mark-fill); }
  .brand__name { display: block; line-height: 1; white-space: nowrap; }
  .brand__sub  { display: block; line-height: 1; white-space: nowrap; }

  .card--front .brand { left: 40px; top: 112px; width: 238px; color: var(--forest); }
  .card--front .brand__mark { width: 144px; height: 144px; }
  .card--front .brand__name { font-size: 29px; margin-top: 8px; }
  .card--front .brand__sub  { font-size: 12px; letter-spacing: 10.5px; margin-top: 4px; padding-left: 10px; }

  .card--back .brand { left: 136px; top: 58px; width: 420px; color: var(--card-white); }
  .card--back .brand__mark { width: 198px; height: 198px; }
  .card--back .brand__name { font-size: 46px; margin-top: 8px; }
  .card--back .brand__sub  { font-size: 19px; letter-spacing: 17px; margin-top: 6px; padding-left: 17px; }

  .divider { position: absolute; left: 296px; top: 113px; width: 1.5px; height: 166px; background: var(--leaf); }

  .details { position: absolute; left: 326px; top: 108px; width: 330px; font-family: "Arimo", sans-serif; color: var(--ink); }
  .person__name { font-family: "Cinzel", serif; font-weight: 700; font-size: 26px; line-height: 1; color: var(--forest); }
  .person__name .surname { color: var(--leaf); }
  .person__role { font-size: 16px; margin-top: 3px; }
  .contact { list-style: none; margin-top: 24px; }
  .contact li { display: flex; align-items: center; font-size: 16px; height: 23px; white-space: nowrap; }
  .contact svg { width: 13px; height: 13px; margin-right: 7px; flex: none; fill: var(--forest); }
  .rule { height: 1px; background: var(--leaf); margin-top: 8px; width: 303px; }
  .tagline { font-size: 16px; margin-top: 8px; }
</style>
</head>
<body>
<div class="stage">
  <section class="card card--front">
    <div class="brand">
      <span class="brand__mark" role="img" aria-label="Company logo mark area"></span>
      <span class="brand__name">MAPLE RIDGE</span>
      <span class="brand__sub">LANDSCAPING</span>
    </div>
    <div class="divider"></div>
    <div class="details">
      <h1 class="person__name">TOBIN <span class="surname">MARSH</span></h1>
      <p class="person__role">Founder/CEO</p>
      <ul class="contact">
        <li><svg viewBox="0 0 16 16"><path d="M3.6 1.2l2.3 2.6-1.3 1.8c.9 2 2.7 3.9 4.8 4.9l1.8-1.3 2.6 2.3-1.4 2.3C7.2 14.6 1.4 8.8 1.3 2.6z"/></svg>555-318-7642</li>
        <li><svg viewBox="0 0 16 16"><path d="M1 3h14v2L8 9 1 5z M1 6.6l7 4 7-4V13H1z"/></svg>service@mapleridgelandscaping.example</li>
        <li><svg viewBox="0 0 16 16"><circle cx="8" cy="8" r="7"/><path d="M5 4c2 1 1 3 3 3s1 3 3 2M9 13c0-2 2-2 3-3" stroke="#fff" stroke-width="1.2" fill="none"/></svg>www.mapleridgelandscaping.example</li>
      </ul>
      <div class="rule"></div>
      <p class="tagline">Lawn &amp; landscape maintenance services</p>
    </div>
  </section>

  <section class="card card--back">
    <div class="brand">
      <span class="brand__mark" role="img" aria-label="Company logo mark area"></span>
      <span class="brand__name">MAPLE RIDGE</span>
      <span class="brand__sub">LANDSCAPING</span>
    </div>
  </section>
</div>
</body>
</html>
```